依頼詳細
道路上に出す看板広告のデザイン制作・2枚分、両方合わせてのデザインをお願いします。(統一感があれば2枚別々のデザインでも可能です)

サイズは[H2730mm×W2730][H2700㎜×W1200㎜]でお願いします。
・シンプルかつ高級な雰囲気
・あまり病院っぽくない広告
・ごちゃごちゃせずスッキリしたデザイン

ほとんどの方が車に乗っている際に見る看板になります。
無痛分娩というワードを強めに出したいと思っています。
記載項目
以下の事項は必ずいれてください。
会社名/住所/電話番号/クリニックのロゴ/診療科
診療科の内訳は、
無痛分娩・不妊治療/産婦人科 としてください。
(無痛分娩+10万円)(不妊治療 自由診療3~4万円)※金額は全て税込み
希望イメージ
シンプル 複雑
単色 カラフル
暗い 明るい
日常 高級
遊び心 厳粛
未来的 伝統的
女性的 男性的
希望する色
青系、水色系
納品ファイル
• イラストレーター形式 (.ai)
補足説明
添付資料の左側が[H2730mm×W2730]、右側が[H2700㎜×W1200㎜]

クリニックのロゴを生かしたデザインで、一際目の引く広告にしていただけたと思っております。

ご提案してくださった皆様、様々なデザインをご提案いただきありがとうございました。
また機会がございましたら、ぜひお願い出来ればと思います。

```html
<!DOCTYPE html>
<html lang="ja">
<head>
<meta charset="utf-8">
<title>汐見レディスクリニック 看板</title>
<link href="https://fonts.googleapis.com/css2?family=Noto+Sans+JP:wght@400;700;900&family=Shippori+Mincho:wght@500&display=swap" rel="stylesheet">
<style>
  :root{
    --teal:#2a87a3;
    --teal-deep:#1f7590;
    --placeholder:#e3e8ea;
    --white:#ffffff;
    --ink:#333b40;
    --canvas:#eef1f2;
  }
  *{margin:0;padding:0;box-sizing:border-box}
  html,body{width:1200px;height:848px;overflow:hidden;background:var(--canvas)}
  body{font-family:"Noto Sans JP",sans-serif;position:relative}

  .sign{position:absolute;top:64px;height:720px;background:var(--white);overflow:hidden;box-shadow:0 4px 18px rgba(0,0,0,.12)}
  .sign--square{left:50px;width:720px}
  .sign--tall{left:830px;width:320px}

  /* square sign */
  .sign__head{height:113px;display:flex;align-items:center;gap:20px;padding:0 26px}
  .badge{background:var(--teal);color:var(--white);font-weight:900;font-size:38px;border-radius:40px;padding:4px 26px;letter-spacing:.04em}
  .departments{color:var(--teal);font-weight:700;font-size:36px;letter-spacing:.04em}
  .sign__body{position:absolute;top:113px;left:0;right:0;bottom:0;background:var(--teal);color:var(--white)}
  .clinic-name{position:absolute;top:26px;left:0;right:0;text-align:center;font-weight:700;font-size:54px;letter-spacing:.08em;line-height:1}
  .rule{position:absolute;top:101px;left:24px;right:24px;height:3px;background:var(--white)}
  .price{position:absolute;left:24px;font-weight:700;font-size:32px;line-height:1}
  .price--birth{top:130px}
  .price--fertility{top:180px}
  .note{position:absolute;left:30px;top:230px;font-size:19px;opacity:.9}
  .info-row{position:absolute;left:24px;display:flex;align-items:center;gap:20px;font-weight:700}
  .info-row--tel{top:308px;font-size:38px}
  .info-row--address{top:364px;font-size:28px}
  .label{display:inline-block;width:82px;text-align:center;background:rgba(255,255,255,.22);border:1.5px solid var(--white);font-size:20px;font-weight:700;padding:3px 0;line-height:1.3}
  .access{position:absolute;right:28px;top:286px;background:var(--white);color:var(--teal);font-weight:700;font-size:22px;padding:8px 16px;border-radius:8px}
  .access::after{content:"";position:absolute;left:26px;bottom:-12px;border:8px solid transparent;border-top:8px solid var(--white);border-left:10px solid var(--white)}
  .photos{position:absolute;left:0;right:0;bottom:0;height:172px;display:flex;gap:6px}
  .photo{flex:1;background:linear-gradient(160deg,#c9b59c 0%,#8d7a66 55%,#5f5346 100%)}
  .photo--b{background:linear-gradient(170deg,#e4e1da 0%,#b9b3a8 50%,#7f766a 100%)}
  .photo--c{background:linear-gradient(165deg,#d9d4cc 0%,#a7a199 50%,#6d665e 100%)}

  /* tall sign */
  .band{position:absolute;left:0;right:0;background:var(--teal)}
  .band--top{top:0;height:20px}
  .band--bottom{bottom:0;height:30px}
  .logo-slot{position:absolute;top:74px;left:35px;width:250px;height:250px;background:var(--placeholder)}
  .wordmark{position:absolute;top:390px;left:0;right:0;text-align:center;font-family:"Shippori Mincho",serif;font-weight:500;color:var(--ink);font-size:46px;line-height:92px;letter-spacing:.28em;text-indent:.28em}
</style>
</head>
<body>
  <section class="sign sign--square">
    <header class="sign__head">
      <span class="badge">無痛分娩</span>
      <span class="departments">不妊治療 / 産婦人科</span>
    </header>
    <div class="sign__body">
      <h1 class="clinic-name">汐見レディスクリニック</h1>
      <div class="rule"></div>
      <p class="price price--birth">【無痛分娩 +10 万円】</p>
      <p class="price price--fertility">【不妊治療 自由診療 3~4 万円】</p>
      <p class="note">※金額は全て税込み</p>
      <div class="access">汐見駅西口すぐ</div>
      <p class="info-row info-row--tel"><span class="label">TEL</span>0465-00-2748</p>
      <p class="info-row info-row--address"><span class="label">所在地</span>神奈川県汐見市青葉町 3-4-7</p>
      <div class="photos">
        <div class="photo photo--a" role="img" aria-label="クリニック待合室の写真"></div>
        <div class="photo photo--b" role="img" aria-label="クリニック受付ロビーの写真"></div>
        <div class="photo photo--c" role="img" aria-label="クリニック院内廊下の写真"></div>
      </div>
    </div>
  </section>

  <section class="sign sign--tall">
    <div class="band band--top"></div>
    <div class="logo-slot" role="img" aria-label="クリニックのロゴマーク位置"></div>
    <p class="wordmark">汐見<br>レディス<br>クリニック</p>
    <div class="band band--bottom"></div>
  </section>
</body>
</html>
```